Church Music Album Cover

We are a Christian church in the OKC metro that is releasing a CD of songs that have connected with our congregation over the past few years. We are a church of about 1500 people of all ages- so while we want the design to be fresh, clean, and attractive- it doesn't have to be overly "youthy" or "edgy." Per the CD distribution company, the art image file you create should be able to be delivered with these requirements met:1400 x 1400 pixels minimum; 3000 x 3000 pixels maximumPNG, GIF, JPG, or JPEG file type72 - 300dpi (300dpi is the best)Less than 25mbRGB color scheme (not CMYK)
Updates

Thanks for submissions thus far. I realize my initial description may have not been the most helpful- and it some ways, I'm not 100% sure what I want. However, I would typically end to stay away from concrete images and tend to lean more towards earthy folk images. I don't even know if that makes sense. One google image search of the word "Grace" brings up individual letters spelling out Grace- each on a card clothes lined to a rope with out of focus lights or candles in the background. Another one had out of focus patio light bulbs lighting up the general text. Not sure why I like those and how they can connect to the theme, but I do. Another one had "Grace" on a pallet wall type background. Hopefully those are helpful suggestions.

Target Market(s)

Young parents- 30-40's

Colors

Requirements
Must have
• Title: Melodies from the River Stone
Nice to have
• Earthy/folky themes.
Should not have
• Bright colors

```html
<!DOCTYPE html>
<html lang="en">
<head>
<meta charset="utf-8">
<title>Melodies from the River Stone – Album Cover</title>
<link rel="stylesheet" href="https://fonts.googleapis.com/css2?family=Anton&display=swap">
<style>
  :root {
    --page-bg: #e6e6e6;
    --teal-deep: #0b3f55;
    --teal-mid: #14697f;
    --teal-glow: #2fb3c4;
    --title-white: #f2f2f2;
    --title-side: #9a9a9a;
    --title-shade: #5c5c5c;
  }
  * { box-sizing: border-box; margin: 0; padding: 0; }
  html, body {
    width: 1200px;
    height: 1000px;
    overflow: hidden;
    background: var(--page-bg);
  }
  .album-cover {
    position: absolute;
    left: 200px;
    top: 100px;
    width: 800px;
    height: 800px;
    overflow: hidden;
    box-shadow: 0 10px 30px rgba(0,0,0,0.18);
  }
  .cover-backdrop {
    position: absolute;
    inset: 0;
    background:
      radial-gradient(ellipse 55% 35% at 50% 55%, rgba(47,179,196,0.55), transparent 70%),
      radial-gradient(ellipse 70% 45% at 50% 22%, rgba(47,179,196,0.35), transparent 75%),
      linear-gradient(180deg, var(--teal-mid) 0%, #136479 45%, var(--teal-deep) 100%);
  }
  .cover-title {
    position: absolute;
    left: 0;
    right: 0;
    top: 250px;
    text-align: center;
    font-family: "Anton", "Oswald", sans-serif;
    font-size: 118px;
    line-height: 1.0;
    letter-spacing: 1px;
    text-transform: uppercase;
    color: var(--title-white);
    text-shadow:
      -1px 1px 0 var(--title-side),
      -2px 2px 0 var(--title-side),
      -3px 3px 0 var(--title-side),
      -4px 4px 0 var(--title-side),
      -5px 5px 0 var(--title-side),
      -6px 6px 0 var(--title-shade),
      -10px 14px 18px rgba(0,0,0,0.45);
  }
  .cover-title span { display: block; }
</style>
</head>
<body>
  <main class="album-cover">
    <div class="cover-backdrop" role="img" aria-label="Concert hall stage with teal beams of light, glowing bokeh dots and an audience in silhouette"></div>
    <h1 class="cover-title">
      <span>Melodies</span>
      <span>From the River</span>
      <span>Stone</span>
    </h1>
  </main>
</body>
</html>
```